Website/Logo Design

We need a logo and website design for an opinion mining startup called VantaLume. Our technology mines the web to automatically discover what people are saying about brands, products, etc. The project we are fielding here is for our informational, public-facing website. In its initial incarnation, it will simply be a vehicle for marketing materials and information on our company and its offerings, but it should be flexible enough to expand as more content/functionality is added.

Some designs we like are:
http://www.tradewhisk.example
http://www.gorvantel.example
http://www.kfz.example
http://www.lintwharf.example
http://moxbarrel.example
http://trundlemq.example
http://www.zopla.example
Updates

All, please try to shy away from using a photo of a person as the focal point of the design.  Our company is more technological than social.

Target Market(s)

Primarily businesses interested in sentiment analysis (typically companies involved in advertising, market research, PR, etc.)

Industry/Entity Type

It Company

Requirements
Must have
• We are looking for a clean, modern, and professional design. This includes a logo, homepage, and internal page if it will differ from the homepage.
Nice to have
• It would be excellent if you could provide an HTML mockup if your design is chosen.
Should not have
• Flash, excessive bells and whistles

```html
<!DOCTYPE html>
<html lang="en">
<head>
<meta charset="utf-8">
<title>VantaLume — we watch the web</title>
<link rel="stylesheet" href="https://fonts.googleapis.com/css2?family=Magra:wght@400;700&family=Arimo:wght@400;700&display=swap">
<style>
  :root{
    --ink:#000;
    --panel:#1c1c1c;
    --panel-edge:#3a3a3a;
    --box:#2b2b2b;
    --white:#ffffff;
    --text:#e8e8e8;
    --tan:#c9b49a;
    --sky:#bcdcf5;
    --mint:#d8f2c8;
    --link:#9fd0ff;
    --more:#f2e08a;
    --orange:#f0821e;
    --grey-mark:#555;
  }
  *{box-sizing:border-box;margin:0;padding:0}
  html,body{width:1200px;height:1200px;overflow:hidden;background:var(--ink)}
  body{font-family:"Arimo",Arial,sans-serif;color:var(--text);position:relative}
  .abs{position:absolute}
  .header-collage{left:0;top:0;width:450px;height:230px;
    background:radial-gradient(ellipse at 25% 35%,#5a6f8a 0%,#3a3f55 35%,#1a1a1f 65%,transparent 85%)}
  .logo-oval{left:915px;top:22px;width:255px;height:166px;border-radius:50%;
    background:radial-gradient(ellipse at center,#ffffff 0%,#f4f4f4 55%,#cfcfcf 85%,#8a8a8a 100%);
    display:flex;align-items:center;justify-content:center;gap:10px}
  .logo-dot{width:18px;height:18px;border-radius:50%;background:#222}
  .logo-name{font-family:"Magra",sans-serif;font-weight:700;font-size:30px;color:#222}
  .nav{left:30px;top:225px;width:1132px;height:120px;
    background:linear-gradient(#0a0a0a,#1e1e1e 60%,#101010)}
  .nav-item{position:absolute;top:20px;display:flex;align-items:center;gap:12px}
  .nav-icon{width:66px;height:86px;border-radius:10px;
    background:linear-gradient(150deg,#f7a04a,#e0600e 60%,#8a3a06)}
  .nav-label{font-family:"Magra",sans-serif;font-weight:700;font-size:16px;line-height:18px;color:var(--white);text-transform:uppercase}
  .tagline{left:30px;top:357px;width:1132px;height:93px;border-radius:8px;
    background:linear-gradient(#333,#1d1d1d);border:1px solid var(--panel-edge)}
  .tagline-tail{left:1055px;top:448px}
  .tagline-text{position:absolute;left:85px;top:22px;font-family:"Magra",sans-serif;font-weight:700;font-size:39px;color:var(--white)}
  .tagline-text .sky{color:var(--sky)} .tagline-text .mint{color:var(--mint)}
  .side-head{left:50px;width:289px;height:25px;background:#2e2e2e;
    font-size:13px;color:var(--white);padding:5px 12px;text-transform:uppercase}
  .news{left:62px;top:507px;width:270px;font-size:13px;line-height:15px;color:var(--white)}
  .news p{margin-bottom:6px}
  .news .more{color:var(--more);text-decoration:underline;padding-left:12px}
  .news .item{margin-bottom:18px}
  .video{left:51px;top:778px;width:288px;height:197px;border:2px solid #888;
    background:linear-gradient(#d9e6f0,#7fa6c8 45%,#3b6f9e 80%,#bdbdbd 80%,#dcdcdc)}
  .video-caption{left:51px;top:990px;width:295px;font-size:13px;line-height:15px;color:var(--white)}
  .quote{font-family:Georgia,serif;font-size:230px;line-height:1;color:var(--grey-mark);font-weight:700}
  .headline{left:400px;top:512px;font-family:"Magra",sans-serif;font-size:34px;line-height:40.5px;color:var(--white);text-transform:uppercase}
  .headline .tan{color:var(--tan)} .headline .sky{color:var(--sky)}
  .body-copy{left:400px;top:697px;width:362px;font-size:14.5px;line-height:19.5px;color:var(--white)}
  .body-copy p{margin-bottom:19px}
  .articles-head{left:864px;top:508px;font-family:"Magra",sans-serif;font-weight:700;font-size:32px;line-height:40px;color:var(--text)}
  .article{left:858px;width:302px;height:86px;border-radius:5px;
    background:linear-gradient(#3a3a3a,#232323);border:1px solid #444;
    display:flex;align-items:center;padding:0 20px;font-size:21px;line-height:25px;color:var(--white)}
  .footer{left:42px;top:1116px;width:1128px;height:63px;border-radius:6px;
    background:linear-gradient(#2a2a2a,#141414);border:1px solid #333}
  .footer-links{position:absolute;left:76px;top:24px;display:flex;gap:25px;font-size:13.5px}
  .footer-links a{color:var(--link);text-decoration:underline}
  .social{position:absolute;left:753px;top:10px;display:flex;gap:22px}
  .social span{width:42px;height:42px;border-radius:4px;display:block}
</style>
</head>
<body>
  <div class="abs header-collage" role="img" aria-label="Collage of social network and web site badges fading into the dark header"></div>

  <div class="abs logo-oval">
    <span class="logo-dot"></span><span class="logo-name">VANTALUME</span>
  </div>

  <nav class="abs nav">
    <div class="nav-item" style="left:80px"><span class="nav-icon" role="img" aria-label="Clipboard with pie chart icon"></span><span class="nav-label">Products<br>&amp; Services</span></div>
    <div class="nav-item" style="left:297px"><span class="nav-icon" role="img" aria-label="Signboard with world map icon"></span><span class="nav-label">About<br>VantaLume</span></div>
    <div class="nav-item" style="left:537px"><span class="nav-icon" role="img" aria-label="Computer monitor icon"></span><span class="nav-label">VantaLume<br>Demo</span></div>
    <div class="nav-item" style="left:760px"><span class="nav-icon" role="img" aria-label="Support team member icon"></span><span class="nav-label">Our<br>Team</span></div>
    <div class="nav-item" style="left:935px"><span class="nav-icon" role="img" aria-label="Circular arrows icon"></span><span class="nav-label">Let's<br>Talk</span></div>
  </nav>

  <div class="abs tagline">
    <div class="tagline-text">VantaLume: <span class="sky">we watch the web,</span> <span class="mint">so you dont have to</span></div>
  </div>
  <svg class="abs tagline-tail" width="50" height="30" viewBox="0 0 50 30"><polygon points="0,0 48,0 46,28" fill="#1d1d1d" stroke="#3a3a3a"/><rect x="1" y="0" width="44" height="3" fill="#1d1d1d"/></svg>

  <div class="abs side-head" style="top:475px">VantaLume &nbsp;News</div>
  <div class="abs news">
    <div class="item">
      <p>5-30-2010<br>VantaLume reaches partnership agreement with Northfield Consulting Group to exchange consulting services to support both company's clients.</p>
      <a class="more">&gt;read more</a>
    </div>
    <div class="item">
      <p>5-20-2010<br>VantaLume launches new website packed with information and support for clients and businesses interested in learning more on how social marketing impacts everyone.</p>
      <a class="more">&gt;read more</a>
    </div>
  </div>

  <div class="abs side-head" style="top:736px">VantaLume &nbsp;Video</div>
  <div class="abs video" role="img" aria-label="Video player still showing a globe covered in city towers"></div>
  <p class="abs video-caption">Chirpline is one of the hotetest social networking tools available. In our most recent video we cover the latest Chirpline trends. &nbsp;Learn what your company can do to set yourself apart from the masses.</p>

  <div class="abs quote" style="left:340px;top:440px">&ldquo;</div>
  <div class="abs quote" style="left:735px;top:600px">&rdquo;</div>
  <div class="abs headline">
    <span class="tan">Enhance</span> your <span class="sky">brand</span><br>
    <span class="tan">Broaden</span> the <span class="sky">market</span><br>
    <span class="tan">Grow</span> your <span class="sky">business</span><br>
    <span class="tan">Expand</span> your <span class="sky">tactics</span>
  </div>

  <div class="abs body-copy">
    <p>Welcome to VantaLume. &nbsp;We apply the latest web trend to track your company, your brand and provide valuable analysis on the best ways to reach your customers via the internet.<br>At vero eos et accusam et justo duo dolores et ea rebum. Stet clita kasd gubergren, no sea takimata sanctus est Lorem ipsum dolor sit amet. Lorem ipsum dolor sit amet, consetetur sadipscing elitr, sed diam nonumy eirmod tempor invidunt ut labore.</p>
    <p>Duis autem vel eum iriure dolor in hendrerit in vulputate velit esse molestie consequat, vel illum dolore eu feugiat nulla facilisis at vero eros et accumsan et iusto odio dignissim qui blandit praesent luptatum zzril delenit augue duis dolore te feugait nulla facilisi. Lorem ipsum dolor sit amet, consectetuer adipiscing elit, sed diam</p>
  </div>

  <h2 class="abs articles-head">VantaLume<br>Recent Articles &amp;<br>White Papers</h2>
  <div class="abs article" style="top:642px">The myths about<br>seach engine optimization</div>
  <div class="abs article" style="top:745px">Protect your brand from an online disaster.</div>
  <div class="abs article" style="top:849px">Friendwall or Chirpline:<br>Which is right for you?</div>
  <div class="abs article" style="top:952px">Why your retail business should stay OFFline.</div>

  <footer class="abs footer">
    <div class="footer-links">
      <a>HOME</a><a>PRODUCTS/SERVICES</a><a>ABOUS US</a><a>VANTALUME DEMO</a><a>OUR TEAM</a><a>CONTACT US</a>
    </div>
    <div class="social">
      <span style="background:#3b5998"></span>
      <span style="background:#5fb8e0"></span>
      <span style="background:#2a5f9e"></span>
      <span style="background:#7a3fa0"></span>
      <span style="background:#d8d8d8"></span>
    </div>
  </footer>
</body>
</html>
```